Website design for labour force (commercial truck driver) company

Looking for a Wordpress template (or design files in conjunction with a free Wordpress template).
Company tag line:
Tenvora – On Demand, Professional Drivers
Real Drivers | Real Standards | Real Results
Logo design has already been completed and is attached

Company provides contract drivers to trucking companies. Target market is both the trucking companies looking for drivers and drivers looking for work.
Design to encompass header / footer and basic page design, navigation menu, home page, contact page. Customer will add content and additional pages over time.

```html
<!DOCTYPE html>
<html lang="en">
<head>
<meta charset="utf-8">
<title>Tenvora – On Demand, Professional Drivers</title>
<link rel="stylesheet" href="https://fonts.googleapis.com/css2?family=Roboto:wght@400;500;700&family=Poppins:wght@400;500;600;700&display=swap">
<style>
:root{
  --green:#12876a;
  --black:#000;
  --white:#fff;
  --ink:#1a1a1a;
  --muted:#555;
  --line:#cfcfcf;
}
*{box-sizing:border-box;margin:0;padding:0}
html,body{width:1200px;height:3630px;overflow:hidden;background:var(--black)}
body{position:relative;font-family:'Roboto',sans-serif;color:var(--white)}
.abs{position:absolute}
a{color:inherit;text-decoration:none}

/* top bar */
.topbar{left:0;top:0;width:1200px;height:65px;background:var(--black);font-size:15px;font-weight:500;letter-spacing:.5px}
.topbar .item{top:22px;display:flex;align-items:center;gap:9px}
.topbar .item b{font-weight:700}
.topbar .social{top:20px;left:1004px;display:flex;gap:13px}
.dot{width:25px;height:25px;border-radius:50%;background:var(--white)}

/* hero */
.hero{left:0;top:65px;width:1200px;height:1040px;background:linear-gradient(160deg,#8f9a86 0%,#4a4d4c 25%,#2a2b2d 55%,#151617 80%,#0b0b0c 100%)}
.brand{display:flex;align-items:center;gap:12px;font-family:'Poppins',sans-serif;font-weight:700;color:var(--ink)}
.brand .mark{border-radius:50%;background:var(--green)}
.hero .brand{left:48px;top:145px;font-size:40px}
.hero .brand .mark{width:58px;height:58px}
.nav{left:482px;top:141px;width:666px;height:70px;border-radius:35px;background:var(--green);border:2px solid #0b4a3a;display:flex;align-items:center;justify-content:space-around;padding:0 20px;font-size:21px;font-weight:500;letter-spacing:1.5px}
.welcome{left:0;width:1200px;text-align:center;letter-spacing:3px;font-weight:500}
.w1{top:864px;font-size:31px}
.w2{top:903px;font-size:32px}
.btn-dark{left:528px;top:981px;width:212px;height:58px;border-radius:29px;background:var(--black);display:flex;align-items:center;justify-content:center;font-size:21px;font-weight:500;letter-spacing:1px}

/* tagline band */
.band{left:0;width:1200px;background:var(--green);display:flex;align-items:center;justify-content:center;font-weight:700;letter-spacing:3px}
.tagline{top:1105px;height:78px;gap:52px;font-size:33px}

/* services */
.services{left:0;top:1183px;width:1200px;height:715px;background:var(--black)}
.sec-title{left:0;width:1200px;text-align:center;font-size:31px;font-weight:500;letter-spacing:4px}
.service{top:1290px;width:340px}
.service svg{margin-left:60px}
.service .label{margin-top:32px;width:264px;height:54px;background:var(--green);clip-path:polygon(0 0,100% 0,90% 100%,0 100%);border-radius:6px 0 0 6px;display:flex;align-items:center;padding-left:36px;font-size:24px;font-weight:500;letter-spacing:2.5px}
.service p{margin-top:24px;font-size:20px;line-height:40px;letter-spacing:1.6px}
.service .outline{margin-top:28px;width:204px;height:60px;border:3px solid var(--white);display:flex;align-items:center;justify-content:center;font-size:25px;font-weight:700;letter-spacing:2px}

/* testimonials */
.testi-band{top:1898px;height:80px;font-size:31px;font-weight:500;letter-spacing:4px}
.testi-area{left:0;top:1978px;width:1200px;height:571px;background:var(--white)}
.card{top:2016px;width:322px;height:452px;background:var(--white);box-shadow:0 2px 10px rgba(0,0,0,.15);font-family:'Poppins',sans-serif;color:var(--ink)}
.card .photo{margin:7px 7px 0;height:195px;border-radius:6px;border:2px solid #555}
.card h3{margin:35px 0 0 27px;font-size:14px;font-weight:600;letter-spacing:-.2px}
.card p{margin:12px 20px 0 27px;font-size:14.5px;line-height:26.5px;color:var(--muted)}
.card .actions{margin:14px 0 0 25px;display:flex;align-items:center}
.card .pill{width:136px;height:46px;border-radius:10px;background:var(--black);color:var(--white);display:flex;align-items:center;justify-content:center;font-family:'Roboto',sans-serif;font-size:19px;font-weight:500;letter-spacing:1.2px}
.card .ico{width:34px;height:34px;border-radius:50%;background:#e8e8e8;display:flex;align-items:center;justify-content:center;margin-left:11px}
.card .ico:first-of-type{margin-left:38px}

/* contact */
.contact{left:0;top:2549px;width:1200px;height:647px;background:radial-gradient(ellipse at 62% 55%,#3a3f3d 0%,#1f2322 40%,#0c0e0e 80%),#0c0e0e}
.field{border-bottom:2px solid var(--line);font-size:20px;letter-spacing:1.8px;padding-bottom:12px}
.btn-green{left:522px;top:3031px;width:168px;height:56px;background:var(--green);clip-path:polygon(0 0,100% 0,88% 100%,0 100%);border-radius:6px 0 0 6px;display:flex;align-items:center;justify-content:center;padding-right:14px;font-size:28px;font-weight:700;letter-spacing:2px}

/* footer */
.footer{left:0;top:3196px;width:1200px;height:434px;background:var(--black)}
.footer .brand{left:48px;top:3224px;font-size:36px;color:var(--white)}
.footer .brand .mark{width:50px;height:50px}
.f-text{left:52px;top:3314px;font-size:21px;line-height:40px;letter-spacing:1.5px}
.f-head{font-size:20px;font-weight:500;letter-spacing:2px}
.f-links{font-size:16px;font-weight:500;letter-spacing:.8px;line-height:48px}
.f-contact{font-size:15px;letter-spacing:.5px;display:flex;align-items:center;gap:14px}
.f-contact b{font-weight:700}
.ring{width:27px;height:27px;border-radius:50%;border:2px solid var(--white)}
.copy{left:398px;top:3524px;font-size:17px;font-weight:500;letter-spacing:.8px}
</style>
</head>
<body>

<header class="abs topbar">
  <div class="abs item" style="left:366px">
    <svg width="20" height="20" viewBox="0 0 24 24"><path fill="#fff" d="M6.6 10.8a15 15 0 0 0 6.6 6.6l2.2-2.2c.3-.3.7-.4 1-.2 1.1.4 2.3.6 3.6.6.6 0 1 .4 1 1V20c0 .6-.4 1-1 1C10.6 21 3 13.4 3 4c0-.6.4-1 1-1h3.5c.6 0 1 .4 1 1 0 1.2.2 2.4.6 3.6.1.3 0 .7-.2 1z"/></svg>
    <span><b>Call now:</b> +0555 010 2040</span>
  </div>
  <div class="abs item" style="left:625px">
    <svg width="20" height="16" viewBox="0 0 20 16"><rect x="1" y="1" width="18" height="14" fill="none" stroke="#fff" stroke-width="2"/><path d="M1 1l9 8 9-8" fill="none" stroke="#fff" stroke-width="2"/></svg>
    <span><b>Email info:</b> hello@tenvora-mail.com</span>
  </div>
  <div class="abs social"><span class="dot"></span><span class="dot"></span><span class="dot"></span><span class="dot"></span></div>
</header>

<section class="abs hero" role="img" aria-label="Photo of a truck driver at the wheel inside a cab"></section>
<div class="abs brand"><span class="mark"></span>Tenvora</div>
<nav class="abs nav"><a>HOME</a><a>SERVICES</a><a>BOOKING</a><a>CONTACT US</a></nav>
<div class="abs welcome w1">WELCOME TO</div>
<h1 class="abs welcome w2">Tenvora – On Demand, Professional Drivers</h1>
<a class="abs btn-dark">Get Started</a>

<div class="abs band tagline"><span>Real Drivers</span><span>Real Standards</span><span>Real Results</span></div>

<section class="abs services"></section>
<h2 class="abs sec-title" style="top:1213px">OUR SERVICES</h2>

<div class="abs service" style="left:58px">
  <svg width="116" height="66" viewBox="0 0 116 66"><rect x="0" y="0" width="78" height="44" fill="#fff"/><path d="M82 14h20l12 16v18H82z" fill="#fff"/><path d="M90 19h11l8 10H90z" fill="#000"/><rect x="0" y="46" width="114" height="4" fill="#fff"/><g fill="#fff" stroke="#000" stroke-width="3"><circle cx="18" cy="55" r="8"/><circle cx="38" cy="55" r="8"/><circle cx="98" cy="55" r="8"/></g></svg>
  <div class="label">LOREM IPSUM</div>
  <p>Lorem ipsum dolor sit amet, consectetur adipiscing elit, sed do eiusmod tempor incididunt ut labore</p>
  <a class="outline">read more</a>
</div>
<div class="abs service" style="left:455px">
  <svg width="116" height="66" viewBox="0 0 116 66"><rect x="0" y="0" width="78" height="44" fill="#fff"/><path d="M82 14h20l12 16v18H82z" fill="#fff"/><path d="M90 19h11l8 10H90z" fill="#000"/><rect x="0" y="46" width="114" height="4" fill="#fff"/><g fill="#fff" stroke="#000" stroke-width="3"><circle cx="18" cy="55" r="8"/><circle cx="38" cy="55" r="8"/><circle cx="98" cy="55" r="8"/></g></svg>
  <div class="label">LOREM IPSUM</div>
  <p>Lorem ipsum dolor sit amet, consectetur adipiscing elit, sed do eiusmod tempor incididunt ut labore</p>
  <a class="outline">read more</a>
</div>
<div class="abs service" style="left:835px">
  <svg width="116" height="66" viewBox="0 0 116 66"><rect x="0" y="0" width="78" height="44" fill="#fff"/><path d="M82 14h20l12 16v18H82z" fill="#fff"/><path d="M90 19h11l8 10H90z" fill="#000"/><rect x="0" y="46" width="114" height="4" fill="#fff"/><g fill="#fff" stroke="#000" stroke-width="3"><circle cx="18" cy="55" r="8"/><circle cx="38" cy="55" r="8"/><circle cx="98" cy="55" r="8"/></g></svg>
  <div class="label">LOREM IPSUM</div>
  <p>Lorem ipsum dolor sit amet, consectetur adipiscing elit, sed do eiusmod tempor incididunt ut labore</p>
  <a class="outline">read more</a>
</div>

<h2 class="abs band testi-band">CUSTOMER TESTIMONIALS</h2>
<section class="abs testi-area"></section>

<article class="abs card" style="left:61px">
  <div class="photo" role="img" aria-label="Photo of a smiling driver standing beside trucks" style="background:linear-gradient(135deg,#d9dcd8,#8a8f88 50%,#b48a55)"></div>
  <h3>LOREM IPSUM DOLOR SIT AMET</h3>
  <p>Lorem ipsum dolor sited consectetur adipiscing elited sed doted eiusmod tempor incididunt ut labore et dolore magna incididunt sed aliqua.</p>
  <div class="actions"><a class="pill">read more</a>
    <span class="ico"><svg width="14" height="14" viewBox="0 0 14 14"><g fill="#000"><circle cx="11" cy="3" r="2.2"/><circle cx="3" cy="7" r="2.2"/><circle cx="11" cy="11" r="2.2"/></g><path d="M11 3L3 7l8 4" stroke="#000" stroke-width="1.4" fill="none"/></svg></span>
    <span class="ico"><svg width="14" height="13" viewBox="0 0 14 13"><path d="M7 12L1.5 6.5A3.2 3.2 0 0 1 7 2.2a3.2 3.2 0 0 1 5.5 4.3z" fill="#000"/></svg></span>
  </div>
</article>
<article class="abs card" style="left:438px">
  <div class="photo" role="img" aria-label="Photo of a driver leaning out of a truck cab window" style="background:linear-gradient(135deg,#e4e6e8,#9ea3a8 50%,#5c5f63)"></div>
  <h3>LOREM IPSUM DOLOR SIT AMET</h3>
  <p>Lorem ipsum dolor sited consectetur adipiscing elited sed doted eiusmod tempor incididunt ut labore et dolore magna incididunt sed aliqua.</p>
  <div class="actions"><a class="pill">read more</a>
    <span class="ico"><svg width="14" height="14" viewBox="0 0 14 14"><g fill="#000"><circle cx="11" cy="3" r="2.2"/><circle cx="3" cy="7" r="2.2"/><circle cx="11" cy="11" r="2.2"/></g><path d="M11 3L3 7l8 4" stroke="#000" stroke-width="1.4" fill="none"/></svg></span>
    <span class="ico"><svg width="14" height="13" viewBox="0 0 14 13"><path d="M7 12L1.5 6.5A3.2 3.2 0 0 1 7 2.2a3.2 3.2 0 0 1 5.5 4.3z" fill="#000"/></svg></span>
  </div>
</article>
<article class="abs card" style="left:815px">
  <div class="photo" role="img" aria-label="Photo of a smiling driver seated at the wheel of a blue truck" style="background:linear-gradient(135deg,#2f4fc4,#1c2d7a 50%,#9a6a3a)"></div>
  <h3>LOREM IPSUM DOLOR SIT AMET</h3>
  <p>Lorem ipsum dolor sited consectetur adipiscing elited sed doted eiusmod tempor incididunt ut labore et dolore magna incididunt sed aliqua.</p>
  <div class="actions"><a class="pill">read more</a>
    <span class="ico"><svg width="14" height="14" viewBox="0 0 14 14"><g fill="#000"><circle cx="11" cy="3" r="2.2"/><circle cx="3" cy="7" r="2.2"/><circle cx="11" cy="11" r="2.2"/></g><path d="M11 3L3 7l8 4" stroke="#000" stroke-width="1.4" fill="none"/></svg></span>
    <span class="ico"><svg width="14" height="13" viewBox="0 0 14 13"><path d="M7 12L1.5 6.5A3.2 3.2 0 0 1 7 2.2a3.2 3.2 0 0 1 5.5 4.3z" fill="#000"/></svg></span>
  </div>
</article>

<section class="abs contact" role="img" aria-label="Photo of a semi truck driving on a highway at dusk"></section>
<h2 class="abs sec-title" style="top:2605px">GET IN TOUCH</h2>
<div class="abs field" style="left:58px;top:2703px;width:439px">First Name:</div>
<div class="abs field" style="left:697px;top:2703px;width:438px">Last Name:</div>
<div class="abs field" style="left:61px;top:2814px;width:436px">Email address:</div>
<div class="abs field" style="left:697px;top:2814px;width:438px">Phone number:</div>
<div class="abs field" style="left:61px;top:2925px;width:1081px">Messages:</div>
<a class="abs btn-green">Submit</a>

<footer class="abs footer"></footer>
<div class="abs brand"><span class="mark"></span>Tenvora</div>
<p class="abs f-text">Lorem ipsum dolor sit amet,<br>consectetur adipiscing elit</p>
<div class="abs f-head" style="left:52px;top:3455px">FOLLOW ON</div>
<div class="abs" style="left:52px;top:3517px;display:flex;gap:31px"><span class="ring"></span><span class="ring"></span><span class="ring"></span><span class="ring"></span></div>

<div class="abs f-head" style="left:432px;top:3222px">QUICKLINKS</div>
<ul class="abs f-links" style="left:435px;top:3250px;list-style:none">
  <li>&gt;&gt; Home</li><li>&gt;&gt; About Us</li><li>&gt;&gt; Services</li><li>&gt;&gt; News</li><li>&gt;&gt; Contact Us</li>
</ul>
<div class="abs f-head" style="left:628px;top:3222px">OTHERLINKS</div>
<ul class="abs f-links" style="left:631px;top:3250px;list-style:none">
  <li>&gt;&gt; Team</li><li>&gt;&gt; FAQ</li><li>&gt;&gt; Services</li><li>&gt;&gt; Privacy</li><li>&gt;&gt; Policy</li>
</ul>
<div class="abs f-head" style="left:818px;top:3222px">CONTACT US</div>
<div class="abs f-contact" style="left:820px;top:3268px">
  <svg width="18" height="18" viewBox="0 0 24 24"><path fill="#fff" d="M6.6 10.8a15 15 0 0 0 6.6 6.6l2.2-2.2c.3-.3.7-.4 1-.2 1.1.4 2.3.6 3.6.6.6 0 1 .4 1 1V20c0 .6-.4 1-1 1C10.6 21 3 13.4 3 4c0-.6.4-1 1-1h3.5c.6 0 1 .4 1 1 0 1.2.2 2.4.6 3.6.1.3 0 .7-.2 1z"/></svg>
  <span><b>Call now:</b> +0555 010 2040</span>
</div>
<div class="abs f-contact" style="left:820px;top:3312px">
  <svg width="20" height="16" viewBox="0 0 20 16"><rect x="1" y="1" width="18" height="14" fill="none" stroke="#fff" stroke-width="2"/><path d="M1 1l9 8 9-8" fill="none" stroke="#fff" stroke-width="2"/></svg>
  <span><b>Email:</b> office@tenvora-mail.com</span>
</div>
<p class="abs copy">© Copyrights 2025 Tenvora All Rights Reserved</p>

</body>
</html>
```